Sunny Trails and joy Business card

I have a logo, but will like a business card design. Is for a travel agency in Mexico. We focus in family experiences.

I will liek some thing different and unique, from the traditional business card, something to get remmeber for.

Business card information:

Leandro R. Quiroga
leandro@sunnytrailsjoy.example

Alameda 742, 3 piso
Col. Tepalcatl
Mexico, D.F. 04910

office: (55) 4821-7390
mobile: (55) 7034-1258

www.sunnytrailsjoy.example
@sunnytjoy
blog: sunnytrailsandjoy.blog.example
facebook: SunnyTrailsAndJoy

```html
<!DOCTYPE html>
<html lang="en">
<head>
<meta charset="utf-8">
<title>Sunny Trails and joy — Business card</title>
<link rel="stylesheet" href="https://fonts.googleapis.com/css2?family=Source+Sans+3:wght@400;700&display=swap">
<style>
  :root {
    --page: #ffffff;
    --card-front: #ffffff;
    --brand-blue: #1b4f9c;
    --sky-light: #cde9f8;
    --sky-mid: #5ecbf2;
    --sky-deep: #5aa6dc;
    --rule: #4b7fa3;
    --ink: #1f2a33;
    --glow: rgba(255, 255, 255, 0.85);
    --map-blue: #1a55a6;
  }
  * { margin: 0; padding: 0; box-sizing: border-box; }
  html, body {
    width: 1200px;
    height: 900px;
    overflow: hidden;
    background: var(--page);
    font-family: "Source Sans 3", "Myriad Pro", sans-serif;
    color: var(--ink);
  }
  .canvas { position: relative; width: 1200px; height: 900px; }

  .card {
    position: absolute;
    left: 343px;
    width: 566px;
    height: 346px;
    border-radius: 18px;
    box-shadow: 0 6px 14px rgba(0, 0, 0, 0.22);
    overflow: hidden;
  }

  /* Front */
  .card--front {
    top: 74px;
    background: var(--card-front);
    border: 1px solid #e4e4e4;
  }
  .brand {
    position: absolute;
    left: 0; right: 0;
    top: 150px;
    display: flex;
    align-items: center;
    justify-content: center;
    gap: 14px;
  }
  .brand__dot {
    width: 30px; height: 30px;
    border-radius: 50%;
    background: var(--sky-mid);
  }
  .brand__name {
    font-weight: 700;
    font-size: 40px;
    color: var(--brand-blue);
    letter-spacing: 0.5px;
  }

  /* Back */
  .card--back {
    top: 486px;
    background: linear-gradient(100deg, var(--sky-light) 0%, var(--sky-mid) 50%, var(--sky-deep) 100%);
  }
  .info-frame {
    position: absolute;
    left: 32px; top: 27px;
    width: 506px; height: 291px;
    border: 1px solid var(--rule);
    border-radius: 18px;
    overflow: hidden;
  }
  .globe-cell {
    position: absolute;
    left: 0; top: 0;
    width: 185px; height: 205px;
    border-right: 1px solid var(--rule);
    border-bottom: 1px solid var(--rule);
    background: radial-gradient(circle at 60% 40%, var(--glow) 0%, rgba(255,255,255,0.25) 55%, rgba(255,255,255,0) 80%);
  }
  .globe-cell__map {
    position: absolute;
    left: 13px; top: 57px;
    width: 160px; height: 82px;
    border-radius: 10px;
    background: var(--map-blue);
  }
  .contact-list {
    position: absolute;
    left: 185px; top: 0;
    width: 321px;
    list-style: none;
  }
  .contact-list__row {
    height: 40px;
    padding-left: 13px;
    display: flex;
    align-items: center;
    font-size: 19px;
    border-bottom: 1px solid var(--rule);
  }
  .contact-list__row--name {
    height: 45px;
    font-size: 23px;
  }
  .contact-list__row:last-child { border-bottom: 1px solid var(--rule); }
  .address-block {
    position: absolute;
    left: 0; right: 0;
    top: 212px;
    text-align: center;
    font-size: 16.5px;
    line-height: 24.5px;
  }
</style>
</head>
<body>
<main class="canvas">
  <section class="card card--front" aria-label="Card front">
    <div class="brand">
      <span class="brand__dot"></span>
      <span class="brand__name">Sunny Trails and joy</span>
    </div>
  </section>

  <section class="card card--back" aria-label="Card back">
    <div class="info-frame">
      <div class="globe-cell">
        <div class="globe-cell__map" role="img" aria-label="World map silhouette in deep blue"></div>
      </div>
      <ul class="contact-list">
        <li class="contact-list__row contact-list__row--name">Leandro R. Quiroga</li>
        <li class="contact-list__row">office: (55) 4821-7390</li>
        <li class="contact-list__row">mobile: (55) 7034-1258</li>
        <li class="contact-list__row">leandro@sunnytrailsjoy.example</li>
        <li class="contact-list__row">www.sunnytrailsjoy.example</li>
      </ul>
      <address class="address-block" style="font-style: normal;">
        Alameda 742, 3 piso, Col. Tepalcatl, Mexico, D.F. 04910<br>
        blog: sunnytrailsandjoy.blog.example<br>
        facebook: SunnyTrailsAndJoy
      </address>
    </div>
  </section>
</main>
</body>
</html>
```